Awesome photographers card for an awesome new business

Double sided business card Black background and silver logo in middle on one side. Details on otherside. please keep it simple

Photographer

Gavin Tolley
0482615073
GavinTolleyPhotography82@lumenpost.com
www.GavinTolleyPhotography.com.au
Instagram _Gavin_tolley

Requirements
Must have
• My logo in Silver
• please use instagram logo instead of "Instagram"

```html
<!DOCTYPE html>
<html lang="en">
<head>
<meta charset="utf-8">
<title>Gavin Tolley Photography – Business Card</title>
<link rel="stylesheet" href="https://fonts.googleapis.com/css2?family=Arimo:wght@400&display=swap">
<style>
  :root {
    --backdrop: #2b2b2b;
    --card: #f1f1f1;
    --silver: #a9a9a9;
    --silver-soft: #b4b4b4;
  }
  * { margin: 0; padding: 0; box-sizing: border-box; }
  html, body {
    width: 1189px; height: 1200px; overflow: hidden;
    background: var(--backdrop);
    font-family: "Arimo", Arial, sans-serif;
  }
  .canvas { position: relative; width: 1189px; height: 1200px; }
  .card {
    position: absolute; left: 171px; width: 856px; height: 490px;
    background: var(--card);
  }
  .card--front { top: 66px; }
  .card--back { top: 625px; }

  .brand-mark {
    position: absolute; left: 0; right: 0;
    text-align: center; color: var(--silver);
    font-weight: 400; text-transform: uppercase;
  }
  .card--front .brand-mark { top: 205px; font-size: 30px; letter-spacing: 6px; line-height: 1.4; }
  .card--back .brand-mark { top: 136px; font-size: 24px; letter-spacing: 5px; line-height: 1.4; }

  .social {
    position: absolute; left: 0; right: 0; top: 426px;
    display: flex; justify-content: center; align-items: center; gap: 20px;
    color: var(--silver); font-size: 22px;
  }
  .social__dot {
    width: 32px; height: 32px; border-radius: 50%;
    background: var(--silver-soft);
  }

  .details {
    position: absolute; left: 0; right: 0; top: 302px;
    text-align: center; color: var(--silver);
  }
  .details__name { font-size: 32px; letter-spacing: 0.5px; line-height: 44px; }
  .details__line { font-size: 21px; line-height: 33px; }
</style>
</head>
<body>
<main class="canvas">
  <section class="card card--front" aria-label="Card front">
    <div class="brand-mark">Gavin Tolley<br>Photography</div>
    <div class="social">
      <span class="social__dot" aria-hidden="true"></span>
      <span class="social__handle">Gavin_tolley</span>
    </div>
  </section>

  <section class="card card--back" aria-label="Card back">
    <div class="brand-mark">Gavin Tolley<br>Photography</div>
    <div class="details">
      <p class="details__name">GAVIN TOLLEY</p>
      <p class="details__line">0482615073</p>
      <p class="details__line">GavinTolleyPhotography82@lumenpost.com</p>
      <p class="details__line">www.GavinTolleyPhotography.com.au</p>
    </div>
  </section>
</main>
</body>
</html>
```